We are launching in December, a range of supplements and vitamins.

We have just made an amend to the mission statement and how we are going to give back to society. Please can you add both to the packaging:

Verdane’s purpose is to support health, wellbeing and longevity, so that we can all thrive in the modern world; an environment so alien to that in which we evolved. Embracing technology, research and science, we harness nature’s goodness - enabling us all to love life – naturally.

Twice Each Day Pledge. For each and every Verdane supplement you take, we provide a supplement to an under nourished child.

For every supplement we sell: £1 goes to the charity ‘Little Lanterns Fund’ and in addition we provide one healthy meal to an under privileged child in India.

My name is Mark Holloway and I own several companies including www.lustrova.com (you can check me out on Infopedon – I am not the football referee nor the rocket scientist, but the entrepreneur) . Over the past 2 years I have been writing a book to help people live more healthily and it launches in December. It’s called Verdane Way. While doing my research for the book, I came to realise that most supplements and vitamin products on the market are rubbish! Most are made for profit and not for the benefit of the consumer. I want to change all of that. Gordon Ashby is patron of a charity I set up with my brother Paul Holloway and together we have built 11 schools in Asia. I am hoping to get Gordons help in getting my supplements to market.

Positioning of our supplements - In a world where so much has changed from the one our bodies were designed to thrive, at Verdane Supplements we are driven by one purpose; to globally provide healthy support to life in the 21st century. While the roots of our wellbeing supplements date back beyond 10,000BC, we embrace modern technology and science, to encapsulate powerful phytonutrients, herbs and other goodness. The essence of which is to promote health, happiness and longevity.

So what are we looking for in the design? Something that stands out. Something that looks professional. A design and concept that can role out across 24 different products. Some products are simple, just one ingredient, such as vitamin D3, Magnesium, Garlic Extracts etc, and others are our own formulas where there are up to 30 different ingredients. You can contact me at any time with questions at Mark@verdaneway.com

Target Market(s)

Male & Female 20 years plus, mainly UK

Industry/Entity Type

Medical

Logo Text

VERDANE - Sub heading = Thriving Days Outdoors

Colors

Designer to choose colors to be used in the design.

Requirements
Must have
• see attached powerpoint.
• We have just made an amend to the mission statement and how we are going to give back to society. Please can you add both to the packaging:
• Verdane’s purpose is to support health, wellbeing and longevity, so that we can all thrive in the modern world; an environment so alien to that in which we evolved. Embracing technology, research and science, we harness nature’s goodness - enabling us all to love life – naturally.
• Twice Each Day Pledge. For each and every Verdane supplement you take, we provide a supplement to an under nourished child.
Nice to have
• see attached powerpoint
Should not have
• see attached powerpoint

```html
<!DOCTYPE html>
<html lang="en">
<head>
<meta charset="utf-8">
<title>Verdane Vitamin D3 – Label Front and Back</title>
<link href="https://fonts.googleapis.com/css2?family=Montserrat:wght@400;500;600;700;800&display=swap" rel="stylesheet">
<style>
  :root {
    --backdrop-light: #f6f6f6;
    --backdrop-dark: #e2e2e2;
    --label-light: #f3f3f3;
    --label-mid: #e6e6e6;
    --brand-navy: #0d2f8f;
    --brand-blue: #2d66c6;
    --ring-grey: #9a9a9a;
    --heading-grey: #6a6a6a;
    --body-text: #6f6f6f;
    --muted-text: #9a9a9a;
    --rule: #c9c9c9;
  }
  * { box-sizing: border-box; margin: 0; padding: 0; }
  html, body { width: 1200px; height: 953px; overflow: hidden; }
  body {
    position: relative;
    background: radial-gradient(ellipse at 50% 40%, var(--backdrop-light) 0%, var(--backdrop-dark) 100%);
    font-family: "Montserrat", sans-serif;
    color: var(--body-text);
  }
  .label {
    position: absolute;
    top: 300px;
    width: 405px;
    height: 465px;
    background: linear-gradient(90deg, var(--label-mid) 0%, var(--label-light) 30%, var(--label-light) 70%, var(--label-mid) 100%);
  }
  .label--front { left: 155px; }
  .label--back { left: 650px; }

  .brand {
    position: absolute;
    top: 60px;
    left: 0;
    width: 100%;
    display: flex;
    justify-content: center;
    align-items: center;
    gap: 10px;
  }
  .brand__dot {
    width: 16px; height: 16px;
    border-radius: 50%;
    background: var(--ring-grey);
  }
  .brand__name {
    font-weight: 800;
    font-size: 28px;
    letter-spacing: 1px;
    color: var(--brand-navy);
  }

  .rule-v { position: absolute; width: 1px; background: var(--rule); }
  .rule-h { position: absolute; height: 1px; background: var(--rule); }

  .copy {
    position: absolute;
    font-size: 10px;
    line-height: 12px;
    color: var(--body-text);
  }
  .copy strong { font-weight: 600; }

  .product-name {
    position: absolute;
    left: 175px;
    top: 262px;
    font-size: 45px;
    font-weight: 500;
    letter-spacing: 1px;
    color: var(--heading-grey);
    line-height: 1;
  }
  .product-code {
    position: absolute;
    left: 170px;
    top: 300px;
    font-size: 138px;
    font-weight: 700;
    letter-spacing: -4px;
    line-height: 1;
  }
  .product-code__letter { color: var(--brand-blue); }
  .product-code__number { color: var(--brand-navy); }

  .spec {
    position: absolute;
    left: 42px;
    font-size: 9px;
    line-height: 11px;
    color: var(--muted-text);
  }
  .spec b { display: block; font-weight: 600; color: var(--body-text); }
  .spec--serving { top: 388px; }
  .spec--weight { top: 421px; }

  .benefits {
    position: absolute;
    left: 43px;
    top: 231px;
    width: 230px;
    font-size: 10px;
    line-height: 11.5px;
  }
  .benefits h3 { font-size: 10px; font-weight: 600; }
  .benefits ul { list-style: none; }
  .benefits li { padding-left: 8px; text-indent: -6px; }
  .benefits li::before { content: "• "; }

  .mission {
    position: absolute;
    left: 125px;
    top: 383px;
    width: 152px;
    height: 68px;
    border: 1px solid var(--rule);
    padding: 3px 4px;
    font-size: 4.3px;
    line-height: 5.2px;
    color: var(--body-text);
  }
  .mission p + p { margin-top: 3px; }
</style>
</head>
<body>

  <section class="label label--front" aria-label="Front label">
    <div class="brand">
      <span class="brand__dot"></span>
      <span class="brand__name">VERDANE</span>
    </div>

    <div class="rule-v" style="left:25px; top:158px; height:96px;"></div>
    <div class="rule-h" style="left:25px; top:194px; width:380px;"></div>

    <p class="copy" style="left:43px; top:166px; width:200px;">
      <strong>Each tablet contains Vitamin D3 at an exceptional 5000iu.</strong>
    </p>
    <p class="copy" style="left:43px; top:211px; width:200px;">
      <strong>Lack of Vitamin D can lead to bone deformities such as rickets in children and bone pain caused by a condition called osteomalacia in adults.</strong>
    </p>

    <h1 class="product-name">VITAMIN</h1>
    <h2 class="product-code"><span class="product-code__letter">D</span><span class="product-code__number">3</span></h2>

    <p class="spec spec--serving">Serving Size:<b>30 Tablets</b></p>
    <p class="spec spec--weight">Net Weight:<b>225mg</b></p>
  </section>

  <section class="label label--back" aria-label="Back label">
    <div class="brand">
      <span class="brand__dot"></span>
      <span class="brand__name">VERDANE</span>
    </div>

    <div class="rule-v" style="left:28px; top:140px; height:78px;"></div>
    <div class="rule-h" style="left:0; top:218px; width:405px;"></div>

    <p class="copy" style="left:43px; top:147px; width:180px;">
      The body creates Vitamin D from direct sunlight on the skin when outdoors but between October and early March we do not get enough Vitamin D from sunlight.
    </p>

    <div class="benefits">
      <h3>Vitamin D contributes to:</h3>
      <ul>
        <li>Normal absorption and utilisation of calcium and phosphorus and the maintenance of normal blood calcium concentrations</li>
        <li>Normal cell division</li>
        <li>Maintenance of normal bone and teeth</li>
        <li>Normal function of the immune system and healthy inflammatory response</li>
        <li>Maintenance of normal muscle function</li>
      </ul>
    </div>

    <p class="spec spec--serving" style="left:43px;">Serving Size:<b>30 Tablets</b></p>
    <p class="spec spec--weight" style="left:43px;">Net Weight:<b>225mg</b></p>

    <div class="mission">
      <p>Verdane’s purpose is to support health, wellbeing and longevity, so that we can all thrive in the modern world; an environment so alien to that in which we evolved. Embracing technology, research and science, we harness nature’s goodness - enabling us all to love life – naturally.</p>
      <p>Twice Each Day Pledge. For each and every Verdane supplement you take, we provide a supplement to an under nourished child.</p>
    </div>
  </section>

</body>
</html>
```